Request for Business Card Design

Hi. My name is Marlena, I am looking for a new business card design for my company, Quillbrook Sensing Systems, LLC. I really like the design you did for Tavel Harvest and was hoping you could do something similar using our full logo and our mark. I am also open to any raised texture design using our mark. I have attached our full logo, which would need to be somewhere on the card, as well as the mark in both outline and full form, as well as our brand colors / guide. The card does not have to be white, as long as our logo and mark appear. I actually like darker colored business cards more, but am open to all options. If you are interested in working with me, please let me know. We would also take the business card design into letterhead design if you can do that.

```html
<!DOCTYPE html>
<html lang="en">
<head>
<meta charset="utf-8">
<title>Quillbrook Sensing Systems – Business Card</title>
<link href="https://fonts.googleapis.com/css2?family=Poppins:wght@300;400;600&display=swap" rel="stylesheet">
<style>
  :root {
    --stage: #0e0e0f;
    --card: #252527;
    --card-dark: #1f1f21;
    --accent: #1c9ccc;
    --text: #f2f2f2;
    --muted: #bdbdbd;
    --rule: #47474a;
  }
  * { margin: 0; padding: 0; box-sizing: border-box; }
  html, body { width: 1200px; height: 820px; overflow: hidden; }
  body {
    background: var(--stage);
    font-family: "Poppins", sans-serif;
    color: var(--text);
    position: relative;
  }
  .card {
    position: absolute;
    width: 540px;
    height: 310px;
    background: var(--card);
    border-bottom: 4px solid var(--accent);
    border-left: 2px solid var(--accent);
    box-shadow: 0 20px 40px rgba(0,0,0,.6);
  }
  .card--front { left: 40px; top: 255px; }
  .card--back { left: 620px; top: 255px; background: var(--card-dark); }

  .wordmark {
    font-family: "Poppins", sans-serif;
    font-weight: 600;
    color: var(--text);
    text-transform: uppercase;
    letter-spacing: 2px;
    line-height: 1.15;
    display: flex;
    align-items: center;
    gap: 12px;
  }
  .wordmark__dot {
    width: 30px; height: 30px; border-radius: 50%;
    background: var(--accent); flex: none;
  }
  .card--front .wordmark {
    position: absolute; left: 200px; top: 48px; font-size: 22px;
  }
  .card--back .wordmark {
    position: absolute; left: 60px; bottom: 64px; font-size: 26px;
  }

  .divider {
    position: absolute; height: 1px; background: var(--rule);
  }
  .divider--wide { left: 200px; right: 40px; top: 150px; }
  .divider--short { left: 40px; width: 150px; top: 226px; }

  .person { position: absolute; left: 40px; top: 170px; }
  .person__name {
    color: var(--accent); font-weight: 600; font-size: 19px;
    text-transform: uppercase; letter-spacing: .5px; line-height: 1.1;
  }
  .person__role { font-weight: 400; font-size: 15px; color: var(--text); }

  .contacts {
    position: absolute; left: 40px; top: 236px;
    list-style: none; font-size: 13px; font-weight: 400; line-height: 19px;
  }
  .contacts li { display: flex; align-items: center; gap: 8px; }
  .contacts svg { width: 13px; height: 13px; fill: var(--accent); flex: none; }

  .address {
    position: absolute; right: 40px; top: 176px;
    text-align: right; font-size: 13px; font-weight: 300; color: var(--muted);
    line-height: 19px;
  }
</style>
</head>
<body>

<section class="card card--front" aria-label="Business card front">
  <div class="wordmark"><span class="wordmark__dot"></span><span>Quillbrook<br>Sensing Systems</span></div>
  <div class="divider divider--wide"></div>

  <div class="person">
    <p class="person__name">Owen Hartley</p>
    <p class="person__role">Managing Director</p>
  </div>
  <div class="divider divider--short"></div>

  <ul class="contacts">
    <li>
      <svg viewBox="0 0 16 16" aria-hidden="true"><path d="M3.5 1l2.5 3-1.5 1.6a9 9 0 0 0 5.9 5.9L12 10l3 2.5-1.6 2.4C7.5 15.4.6 8.5 1.1 2.6z"/></svg>
      <span>044-987 321 654</span>
    </li>
    <li>
      <svg viewBox="0 0 16 16" aria-hidden="true"><path d="M1 3h14v10H1zm1.5 1.3V5l5.5 4 5.5-4v-.7L8 8.2z"/></svg>
      <span>info@quillbrook.com</span>
    </li>
    <li>
      <svg viewBox="0 0 16 16" aria-hidden="true"><path d="M8 1a7 7 0 1 0 0 14A7 7 0 0 0 8 1zm0 1.3c.9.8 1.6 2.3 1.8 4H6.2c.2-1.7.9-3.2 1.8-4zM2.4 7.3h2.5a11 11 0 0 1 .3-3.6 5.7 5.7 0 0 0-2.8 3.6zm0 1.4a5.7 5.7 0 0 0 2.8 3.6 11 11 0 0 1-.3-3.6zm3.8 0h3.6c-.2 1.7-.9 3.2-1.8 4-.9-.8-1.6-2.3-1.8-4zm4.9 0a11 11 0 0 1-.3 3.6 5.7 5.7 0 0 0 2.8-3.6zm2.5-1.4a5.7 5.7 0 0 0-2.8-3.6c.2 1.1.3 2.3.3 3.6z"/></svg>
      <span>www.quillbrooksensing.com</span>
    </li>
  </ul>

  <p class="address">88, Larkspur Avenue<br>30917, Eastmoor</p>
</section>

<section class="card card--back" aria-label="Business card back">
  <div class="wordmark"><span>Quillbrook<br>Sensing Systems</span></div>
</section>

</body>
</html>
```